Thriving Mexican import business needs a new business card

Need a refresher of our current business card. Looking for a lighter background with the logo on one side. We will want this file to be adjustable so we can change names, emails and mobile numbers.
We are open to ideas but maintaining a professional image is critical.
Thankyou,

Target Market(s)

Anyone in food industry

Industry/Entity Type

Wholesale

Contact Information for Business Card

Mark Pendlebury
Director
Condor Provisions & Spirits Pty Ltd
5B Morrow Ct, Kelvinbrook VIC 3127
0421930576 (03) 95128460
mark@condorlatino.example.au
condorlatinoprovisionsandspirits.example.au

Font styles to use
Serif
Other font styles liked:
• NeoGram Heavy

Requirements
Must have
• Professional yet memorable
Condor logo
Nice to have
• Chilli or tequila/mexican food pictures
Should not have
• Dark background

```html
<!DOCTYPE html>
<html lang="en">
<head>
<meta charset="utf-8">
<title>Condor Provisions &amp; Spirits – Business Card</title>
<link rel="stylesheet" href="https://fonts.googleapis.com/css2?family=Bebas+Neue&display=swap">
<style>
  :root {
    --backdrop: #e6e4e1;
    --flag-green: #116643;
    --flag-white: #f4f4f4;
    --flag-red: #c92027;
    --card-white: #f4f4f4;
    --ink: #1b1b1b;
    --rule: #2a2a2a;
    --chilli-red: #d9261c;
    --chilli-yellow: #f2b51c;
    --chilli-green: #5f9a2c;
  }
  * { box-sizing: border-box; margin: 0; padding: 0; }
  html, body {
    width: 1200px; height: 960px; overflow: hidden;
    background: var(--backdrop);
  }
  .canvas { position: relative; width: 1200px; height: 960px; }
  .card {
    position: absolute; left: 336px; width: 531px; height: 323px;
    box-shadow: 0 3px 8px rgba(0,0,0,.25);
    overflow: hidden;
    font-family: "Bebas Neue", "Oswald", sans-serif;
    color: var(--ink);
  }

  /* Front */
  .card-front { top: 141px; display: flex; }
  .band { height: 100%; width: 177px; }
  .band-green { background: var(--flag-green); }
  .band-white { background: var(--flag-white); }
  .band-red { background: var(--flag-red); flex: 1; }
  .front-brand {
    position: absolute; left: 177px; top: 150px; width: 177px;
    display: flex; align-items: center; justify-content: center; gap: 8px;
  }
  .brand-square { width: 14px; height: 14px; background: var(--ink); }
  .front-brand .brand-name { font-size: 54px; line-height: 1; letter-spacing: 1px; }
  .front-shadow {
    position: absolute; left: 197px; top: 224px; width: 137px; height: 6px;
    border-radius: 50%;
    background: radial-gradient(ellipse at center, rgba(0,0,0,.28), rgba(0,0,0,0) 70%);
  }
  .chilli-skewer {
    position: absolute; left: 134px; top: 256px; width: 265px; height: 26px;
    border-radius: 13px;
    background: linear-gradient(90deg, var(--chilli-red), var(--chilli-yellow) 35%, var(--chilli-red) 60%, var(--chilli-yellow) 75%, var(--chilli-green));
  }

  /* Back */
  .card-back { top: 496px; background: var(--card-white); }
  .back-brand {
    position: absolute; right: 294px; top: 92px;
    display: flex; align-items: center; gap: 8px;
  }
  .back-brand .brand-name { font-size: 44px; line-height: 1; letter-spacing: 1px; }
  .holder { position: absolute; right: 294px; top: 195px; text-align: right; }
  .holder-name { font-size: 19px; line-height: 1; letter-spacing: .3px; }
  .holder-role { font-size: 12px; line-height: 1; margin-top: 6px; }
  .divider {
    position: absolute; left: 264px; top: 89px; width: 1.5px; height: 145px;
    background: var(--rule);
  }
  .company { position: absolute; left: 287px; top: 97px; font-size: 13px; line-height: 18px; }
  .contact-list {
    position: absolute; left: 287px; top: 163px; list-style: none;
    font-size: 13px; line-height: 17.5px;
  }
  .contact-list li { display: flex; align-items: center; gap: 5px; }
  .contact-list svg { width: 11px; height: 11px; flex: none; }
</style>
</head>
<body>
<main class="canvas">

  <section class="card card-front" aria-label="Card front">
    <div class="band band-green"></div>
    <div class="band band-white"></div>
    <div class="band band-red"></div>
    <div class="front-brand">
      <span class="brand-square"></span>
      <span class="brand-name">CONDOR</span>
    </div>
    <div class="front-shadow"></div>
    <div class="chilli-skewer" role="img" aria-label="Photo of a skewer of sliced red, yellow and green chillies"></div>
  </section>

  <section class="card card-back" aria-label="Card back">
    <div class="back-brand">
      <span class="brand-square"></span>
      <span class="brand-name">CONDOR</span>
    </div>
    <div class="holder">
      <p class="holder-name">MARK PENDLEBURY</p>
      <p class="holder-role">DIRECTOR</p>
    </div>
    <div class="divider"></div>
    <p class="company">CONDOR PROVISIONS &amp; SPIRITS PTY LTD<br>5B MORROW CT, KELVINBROOK VIC 3127</p>
    <ul class="contact-list">
      <li>
        <svg viewBox="0 0 12 12" aria-hidden="true"><path d="M2.5 1 L4.5 1 L5.2 3.6 L4 4.6 Q5 7 7.4 8 L8.4 6.8 L11 7.5 L11 9.5 Q11 11 9.5 11 Q1 10 1 2.5 Q1 1 2.5 1Z" fill="#1b1b1b"/></svg>
        0421930576
      </li>
      <li>
        <svg viewBox="0 0 12 12" aria-hidden="true"><rect x="3" y="0.8" width="6" height="10.4" rx="1" fill="none" stroke="#1b1b1b" stroke-width="1.2"/><circle cx="6" cy="9.4" r=".7" fill="#1b1b1b"/></svg>
        (03) 95128460
      </li>
      <li>
        <svg viewBox="0 0 12 12" aria-hidden="true"><rect x="0.8" y="2.3" width="10.4" height="7.4" fill="none" stroke="#1b1b1b" stroke-width="1.2"/><path d="M1 2.6 L6 6.6 L11 2.6" fill="none" stroke="#1b1b1b" stroke-width="1.2"/></svg>
        MARK@CONDORLATINO.EXAMPLE.AU
      </li>
      <li>
        <svg viewBox="0 0 12 12" aria-hidden="true"><g fill="none" stroke="#1b1b1b" stroke-width="1"><circle cx="6" cy="6" r="5"/><ellipse cx="6" cy="6" rx="2.2" ry="5"/><path d="M1 6 H11 M2 3.4 H10 M2 8.6 H10"/></g></svg>
        CONDORLATINOPROVISIONSANDSPIRITS.EXAMPLE.AU
      </li>
    </ul>
  </section>

</main>
</body>
</html>
```